New Print Material Needed for Renovation Company

We are looking to update our current Print Material to reflect the current process we offer to our clients. A lot of the information is also outdated along with many of the photos that are currently being used. We are a renovation company that specializes in residential and commercial renovations and custom builds.This project is MULTIPLE pages. We will pay the chosen designer an extra fee for the designing 3-4 additional pages that are similar to the chosen design. Attached is our current Print Material. We are hoping to update the look of them and some of the messaging. Our current company colors are white, blue and light grey and it will remain that way.

Industry/Entity Type

Construction Company

Font styles to use
Sans Serif

Colors
3176b5
ffffff

Requirements
Must have
• Easy to explain the process
• Easy to read and understand let alone
• Easy to navigate
Nice to have
• As much creativity as possible
Should not have
• no confusing text
• no confusing layout

```html
<!DOCTYPE html>
<html lang="en">
<head>
<meta charset="utf-8">
<title>Our Process – Harbourline Renovation Builders</title>
<link rel="stylesheet" href="https://fonts.googleapis.com/css2?family=Source+Sans+3:wght@400;700;800&family=Noto+Sans:wght@400&display=swap">
<style>
  :root{
    --brand-blue:#1264a3;
    --deep-blue:#155d97;
    --ink-blue:#1b5c96;
    --pale-blue:#dce6f1;
    --step-grey:#9ea3a8;
    --white:#ffffff;
    --body-ink:#1d1d1d;
    --dot:#a7abaf;
  }
  *{margin:0;padding:0;box-sizing:border-box}
  html,body{width:1200px;height:1000px;overflow:hidden;background:var(--white)}
  .sheet{position:relative;width:1200px;height:1000px;font-family:"Noto Sans",sans-serif}
  .process-panel{position:absolute;left:52px;top:0;width:1096px;height:955px;background:var(--brand-blue)}
  .centre-strip{position:absolute;left:490px;top:0;width:110px;height:955px;background:var(--white)}
  .step-backdrop{position:absolute;left:600px;top:0;width:494px;height:805px;background:var(--step-grey)}
  .brand-block{position:absolute;left:600px;top:805px;width:548px;height:150px;background:var(--deep-blue)}

  .phase-label{position:absolute;left:88px;writing-mode:vertical-rl;font-family:"Source Sans 3",sans-serif;
    font-weight:800;color:var(--white);font-size:54px;line-height:1;letter-spacing:32px}
  .phase-design{top:-2px}
  .phase-plan{top:258px}
  .phase-build{top:596px}

  .phase-group{position:absolute;left:137px;width:350px;background:var(--pale-blue)}
  .group-design{top:0;height:172px}
  .group-plan{top:190px;height:334px}
  .group-build{top:541px;height:353px}

  .stage{position:absolute;left:13px;width:324px;font-family:"Source Sans 3",sans-serif}
  .stage-title{font-weight:800;font-size:24px;line-height:24px;color:var(--ink-blue);letter-spacing:.4px;text-transform:uppercase}
  .stage-time{font-weight:400;font-size:20px;line-height:20px;color:var(--ink-blue);margin-top:6px;letter-spacing:.3px}
  .stage-bar{position:absolute;left:0;width:323px;height:28px;background:var(--white)}

  .step-card{position:absolute;left:603px;width:479px;height:96px;background:var(--white);border:3px solid var(--brand-blue);
    padding:8px 10px 0 40px;font-size:21.5px;line-height:23.5px;color:var(--body-ink)}
  .step-num{position:absolute;left:565px;width:64px;height:64px;border-radius:50%;background:var(--brand-blue);
    border:3px solid var(--white);box-shadow:0 0 0 2px var(--brand-blue);color:var(--white);
    font-family:"Source Sans 3",sans-serif;font-weight:800;font-size:38px;line-height:58px;text-align:center}

  .connectors{position:absolute;left:0;top:0}
  .brand-name{position:absolute;left:848px;top:836px;color:var(--white);font-family:"Noto Sans",sans-serif;
    font-weight:400;font-size:25px;line-height:28px}
  .brand-mark{position:absolute;left:738px;top:830px;width:88px;height:88px;border-radius:50%;border:7px solid var(--white)}
</style>
</head>
<body>
<div class="sheet">
  <div class="process-panel"></div>
  <div class="centre-strip"></div>
  <div class="step-backdrop"></div>
  <div class="brand-block"></div>

  <div class="phase-label phase-design">IGN</div>
  <div class="phase-label phase-plan">PLAN</div>
  <div class="phase-label phase-build">BUILD</div>

  <section class="phase-group group-design">
    <div class="stage" style="top:-18px"><div class="stage-time">1-2 WEEKS</div></div>
    <div class="stage-bar" style="left:13px;top:5px"></div>
    <div class="stage" style="top:50px"><div class="stage-title">Final Design<br>(Plan + Scope)</div><div class="stage-time" style="margin-top:14px">1-3 WEEKS</div></div>
    <div class="stage-bar" style="left:13px;top:128px"></div>
  </section>

  <section class="phase-group group-plan">
    <div class="stage" style="top:10px"><div class="stage-title">Material Selection</div><div class="stage-time" style="margin-top:12px">1-4 WEEKS</div></div>
    <div class="stage-bar" style="left:13px;top:67px"></div>
    <div class="stage" style="top:113px"><div class="stage-title">Engineer Drawings</div><div class="stage-time" style="margin-top:12px">2-4 WEEKS</div></div>
    <div class="stage-bar" style="left:13px;top:170px"></div>
    <div class="stage" style="top:213px"><div class="stage-title">Complete Building<br>Permit Plans</div><div class="stage-time" style="margin-top:14px">3-25 WEEKS</div></div>
    <div class="stage-bar" style="left:13px;top:294px"></div>
  </section>

  <section class="phase-group group-build">
    <div class="stage" style="top:10px"><div class="stage-title">Finalization of<br>Materials</div><div class="stage-time" style="margin-top:14px">2-4 WEEKS</div></div>
    <div class="stage-bar" style="left:13px;top:91px"></div>
    <div class="stage" style="top:134px"><div class="stage-title">Final Docs +<br>Construction Plans</div><div class="stage-time" style="margin-top:14px">2-6 WEEKS</div></div>
    <div class="stage-bar" style="left:13px;top:215px"></div>
    <div class="stage" style="top:257px"><div class="stage-title">Scheduling</div><div class="stage-time" style="margin-top:12px">2-4 WEEKS</div></div>
    <div class="stage-bar" style="left:13px;top:315px"></div>
  </section>

  <svg class="connectors" width="1200" height="1000" viewBox="0 0 1200 1000" aria-hidden="true">
    <g fill="var(--brand-blue)">
      <polygon points="487,88 505,100 487,112"/>
      <polygon points="487,218 505,230 487,242"/>
      <polygon points="487,313 505,325 487,337"/>
      <polygon points="487,441 505,453 487,465"/>
      <polygon points="487,588 505,600 487,612"/>
      <polygon points="487,720 505,732 487,744"/>
      <polygon points="487,817 505,829 487,841"/>
    </g>
    <g fill="none" stroke="var(--dot)" stroke-width="3.5" stroke-dasharray="3.5 4">
      <path d="M506 100 H548 V85 H566"/>
      <path d="M506 230 H550 V197 H566"/>
      <path d="M506 325 H548 V307 H566"/>
      <path d="M506 453 H548 V412 H566"/>
      <path d="M506 600 H522 V527 H566"/>
      <path d="M506 732 H515 V636 H566"/>
      <path d="M506 829 H553 V735 H566"/>
    </g>
  </svg>

  <div class="step-card" style="top:-60px;height:97px;padding-top:64px">with your design ideas.</div>
  <div class="step-num" style="top:-42px">2</div>

  <div class="step-card" style="top:50px">Any last minute or final revisions will be completed within three days of this meeting.</div>
  <div class="step-num" style="top:65px">3</div>

  <div class="step-card" style="top:157px">Our material selection coordinator will work with you to ensure all the right materials.</div>
  <div class="step-num" style="top:172px">4</div>

  <div class="step-card" style="top:265px">The final permit drawings will be sent to engineers to ensure structural integrity.</div>
  <div class="step-num" style="top:280px">5</div>

  <div class="step-card" style="top:373px">Permit drawings will begin once the build has been signed and initial payments have been made.</div>
  <div class="step-num" style="top:386px">6</div>

  <div class="step-card" style="top:480px">A lead designer will finalized any revisions you may have for your material section.</div>
  <div class="step-num" style="top:494px">7</div>

  <div class="step-card" style="top:588px;padding-left:36px">The drawings will be updated within 24 hours once the permits have been approved &amp; recived.</div>
  <div class="step-num" style="top:604px">8</div>

  <div class="step-card" style="top:697px;padding-left:36px">All designs, dates, permits have been completed. The project is ready to get underway.</div>
  <div class="step-num" style="top:710px">9</div>

  <div class="brand-mark"></div>
  <div class="brand-name">Harbourline<br>Renovation<br>Builders</div>
</div>
</body>
</html>
```